Catering and Cleaning Company requires brochure

We need a brochure for a catering and cleaning company, the copy should be based on the one uploaded, however the logo has been updated to the one enclosed, and we need it to be revamped for the 21st century.

The Brochure has to fit on an A4 sheet of paper but can be folded or arranged in any way that you want,

```html
<!DOCTYPE html>
<html lang="en">
<head>
<meta charset="utf-8">
<title>Harbourline Services &amp; Catering – Brochure</title>
<link href="https://fonts.googleapis.com/css2?family=Open+Sans:ital,wght@0,400;0,600;0,700;1,700&display=swap" rel="stylesheet">
<style>
  :root{
    --page-bg:#eeeeee;
    --panel-grey:#8b8d90;
    --panel-white:#ffffff;
    --ink:#3a3a3a;
    --ink-light:#ffffff;
    --accent-blue:#3c86c8;
    --hex-grey:#8e8f92;
    --photo-dark:#4a4a4a;
    --photo-light:#bfbfbf;
  }
  *{box-sizing:border-box;margin:0;padding:0}
  html,body{width:1200px;height:900px;overflow:hidden}
  body{background:var(--page-bg);font-family:"Open Sans",Arial,sans-serif;color:var(--ink)}
  .brochure{position:absolute;left:20px;top:40px;width:1160px;height:820px;display:flex;box-shadow:0 6px 24px rgba(0,0,0,.18)}
  .panel{width:33.333%;height:100%;position:relative;overflow:hidden}
  .panel--grey{background:var(--panel-grey);color:var(--ink-light)}
  .panel--white{background:var(--panel-white)}
  .panel--white + .panel--white{border-left:1px solid #e4e4e4}
  .panel-photo{height:120px;width:100%}
  .photo-mono{background:linear-gradient(135deg,var(--photo-dark),var(--photo-light) 55%,#777)}
  .photo-kitchen{background:linear-gradient(120deg,#c9b48a,#e8e2d6 45%,#d8c36a 80%,#b59a3c)}
  .panel-body{padding:16px 22px 0}
  .copy{font-size:9.6px;line-height:1.38;margin-bottom:9px}
  .heading{color:var(--accent-blue);font-weight:700;text-transform:uppercase;font-size:10.5px}
  .panel--grey .heading{color:#4b8fcc}
  .value-name{font-weight:700;font-size:10.5px}
  .tagline{font-weight:700;font-style:italic;font-size:12px;line-height:1.35;margin-top:6px}
  .hex-group{display:block;margin:6px auto 10px}
</style>
</head>
<body>
<main class="brochure">

  <section class="panel panel--grey">
    <div class="panel-photo photo-mono" role="img" aria-label="Black and white photo of catering staff preparing food"></div>
    <div class="panel-body">
      <p class="copy"><span class="heading">About us //</span> Established in 1980, Harbourline Services &amp; Catering, a subsidiary unit of Harbourline Contracting Group, providing catering and gas facilities services to the onshore and offshore oil and gas service institutions before expanding operations to cater to a wider spectrum of clientele including but not limited to, labour camps, hotel staff, construction, education, healthcare and Government facilities and institutions.</p>
      <p class="copy"><span class="heading">Our vision //</span> Our Vision is to provide a world-class service, to partner with our clients in order to excel in the provision of contract catering and support services with a team and facilities of a standard of excellence to help us to exceed expectations.</p>
      <p class="copy"><span class="heading">Our mission //</span> To offer exceptional client value, by ensuring the highest quality of service delivery, implementing balanced solutions and being a preferred supplier across the spectrum of clients whilst ensuring the strictest and highest standards of food control and hygiene, governed by our HACCP, HSE and ISO9001 policies.</p>
      <p class="copy"><span class="heading">Our values //</span><br><span class="value-name">Integrity:</span> integrity is central to what we do and our understanding of integrity is holistic: we are responsible for achieving what we promise to do and we strive to exceed expectations. Integrity ensures the quality of our work, processes, procedures and our staff, as well as the ethical standards of our organisation. Integrity goes hand in hand with honesty, and it is our transparent approach to that helps ensure their continued business.</p>
      <p class="copy"><span class="value-name">Professionalism:</span> with integrity comes professionalism. We exercise professionalism in our operations, our interactions with our clients, our policies, our procedures and in our staff. Our attitude is one that strives for teamwork, reliability, continual improvement and accountability.</p>
      <p class="copy"><span class="value-name">Dedication:</span> dedication is a value which permeates every aspect of our business, from the highest levels of management down. We strive to play a part in our client’s success. We safeguard our partners’ success by going the extra mile, putting in the time and effort required to meet deadlines on time and on budget.</p>
      <p class="tagline">“Nutritionally, satisfying food delivered anywhere, to perfection, on time!”</p>
    </div>
  </section>

  <section class="panel panel--white">
    <div class="panel-photo photo-mono" role="img" aria-label="Black and white photo of a commercial kitchen with trays and equipment"></div>
    <div class="panel-body">
      <p class="copy"><span class="heading">Who we are //</span> Harbourline Services and Catering is all about great food and great service! It’s about listening to what our clients and customers need. It’s about making people feel cared for and looked after. Because we believe service is an honourable profession.</p>
      <p class="copy">At Harbourline we love working with our clients to create a bespoke experience for all involved. Our highly dedicated and professional team make sure the food we produce looks and tastes utterly beautiful and that every aspect of your catering requirement is managed carefully to meet and exceed your standards and expectations!</p>
      <p class="copy"><span class="heading">What we do //</span> From our humble beginnings in 1980 serving the offshore and onshore oil and gas service companies, we have grown thanks to the support of our partners and clients, which has allowed us to extend our culinary operations and expertise to cover the larger spectrum of clientele to include labour camps, hotel staff, construction, education, healthcare and Government.</p>
      <p class="copy">We will work with you to ensure that all of your catering requirements are taken care of and handled every step of the way and will ensure that we accommodate all of the various nationalities and tastes whilst always ensuring a healthy, hygienic and clean environment, adhering to the strictest HACCP policies for food safety in preparation and environment.</p>
      <p class="copy">Fostering relationships with our clients and partners is at the core of our business and has played a key part in our growth. By managing our clients’ catering needs, we allow our clients to concentrate on their core business.</p>
      <p class="copy"><span class="heading">Service pride //</span> We are successful for one very simple reason; because we value our reputation for quality and service. We work hard to build long term relationships with our clients. We listen to their needs and work hard to meet their requirements. We deliver on our promises. We value our people and the communities that we serve.</p>
      <p class="copy">We live by the mantra of teamwork, pride and commitment, together with the combination of expertise, quality and innovation, we will produce high quality masterpieces and culinary excellences whilst ensuring a quality of service and satisfaction to our customers.</p>
      <p class="copy"><span class="heading">Team pride //</span> A team of passionate, qualified and highly experienced professionals, who show utmost commitment to our clients and partners whilst always working to fully certified HACCP methodologies to the highest hygiene levels.</p>
    </div>
  </section>

  <section class="panel panel--white">
    <div class="panel-photo photo-kitchen" role="img" aria-label="Photo of chefs working in a bright production kitchen"></div>
    <div class="panel-body">
      <p class="copy">We recognise that our employees are the principal assets of the company. As such, we focus on their training needs, instil the values of professionalism, integrity and teamwork, provide career opportunities, and reward outstanding performance. Our values are based upon a passion for service and determination to continually improve so we ensure customer satisfaction throughout. We take care of the quality of people we employ, ensure they are well cared for resulting in high morale and, importantly, bringing creativity and initiative to their work.</p>
      <svg class="hex-group" width="300" height="140" viewBox="0 0 300 140" aria-hidden="false">
        <defs>
          <linearGradient id="hexPhoto" x1="0" y1="0" x2="1" y2="1">
            <stop offset="0" stop-color="#8a8f8c"/>
            <stop offset=".5" stop-color="#d9dcd9"/>
            <stop offset="1" stop-color="#6f7370"/>
          </linearGradient>
        </defs>
        <polygon role="img" aria-label="Photo of cooks stirring large kitchen cauldrons" points="40,5 135,5 175,70 135,135 40,135 0,70" fill="url(#hexPhoto)"/>
        <polygon points="188,62 228,62 248,96 228,130 188,130 168,96" fill="var(--hex-grey)"/>
        <polygon points="240,22 278,22 298,56 278,90 240,90 220,56" fill="var(--hex-grey)"/>
      </svg>
      <p class="copy"><span class="heading">Menu &amp; capacity //</span> Our Abu Dhabi central kitchen currently has the capacity to produce over 25,000 meals a day, 7 days a week, 365 days a year. That is almost 9 million meals a year. Your location is not a barrier or deterrent for our operations as we have served off shore clients too! You can be confident that we understand exactly what you need. We are always able to deploy a fully operational team on your site that will operate the kitchen!</p>
      <p class="copy">Menu variation is tailored to the origins of our customers considering personal tastes and preferences and bringing a personal touch to those we live with and serve on site. We offer a wide range of multi ethnic menus, all of which are nutritionally balanced to provide the work force with healthy meals.</p>
      <p class="copy">Menus are designed with daily multiple and well balanced choices to avoid repetition against guiding principles of taste, consistency and variety. Special menus are developed for special events, festive periods and other national holidays. Menu ingredients and methods of preparation meet the ethnic, religious and cultural requirements of a multi-national clientele.</p>
    </div>
  </section>

</main>
</body>
</html>
```